Quorvane Capital Modern Business Card

We need a modern business card template designed for Quorvane Capital.
Quorvane Capital is a diversified global cryptocurrency investment fund.

The font under the logo: Hiragino Kaku Gothic Pro

Color Hexcode: Main colors white (ffffff) & teal (188383), we are open to adding #fcca46 as an accent

Target Market(s)

Accredited Investors, high net worth individuals and institutional investors

Industry/Entity Type

Investment

Contact Information for Business Card

Contact Information should contain
Name
main phone +1 720 555 0147
cell
email

Font styles to use
Sans Serif
Other font styles liked:
• Hiragino Kaku Gothic Pro

Requirements
Must have
• would like to have icons that identify the contact information
• include our website: www.quorvanecapital.example
• include our Tagline: Diversified Crypto Investment Funds
Nice to have
• Would like to have a simple back side with the logo (without the words) and plenty of space

```html
<!DOCTYPE html>
<html lang="en">
<head>
<meta charset="utf-8">
<title>Quorvane Capital — Business Card</title>
<link rel="stylesheet" href="https://fonts.googleapis.com/css2?family=Noto+Sans+JP:wght@400;700&display=swap">
<style>
  :root {
    --teal: #1f9595;
    --white: #ffffff;
    --paper-light: #fafafa;
    --paper-shade: #e6e6e6;
    --ink: #1e1e1e;
    --rule: #111111;
    --backdrop: #e8ecec;
  }
  * { box-sizing: border-box; margin: 0; padding: 0; }
  html, body {
    width: 1200px;
    height: 900px;
    overflow: hidden;
  }
  body {
    background: var(--backdrop);
    font-family: "Noto Sans JP", "Helvetica Neue", Arial, sans-serif;
    position: relative;
  }
  .business-card {
    position: absolute;
    left: 100px;
    top: 142px;
    width: 1000px;
    height: 616px;
    overflow: hidden;
    box-shadow: 0 18px 40px rgba(0, 0, 0, 0.16);
  }
  .card-shapes {
    position: absolute;
    inset: 0;
    width: 100%;
    height: 100%;
  }
  .holder-name {
    position: absolute;
    left: 58px;
    top: 88px;
    color: var(--white);
    font-weight: 700;
    font-size: 34px;
    letter-spacing: 0.5px;
  }
  .contact-list {
    position: absolute;
    left: 58px;
    top: 270px;
    list-style: none;
    color: var(--white);
    font-size: 26px;
    line-height: 36.5px;
  }
  .contact-item {
    display: flex;
    align-items: center;
    gap: 6px;
  }
  .contact-icon {
    width: 22px;
    height: 22px;
    flex: none;
    fill: var(--white);
  }
  .tagline {
    position: absolute;
    left: 58px;
    top: 440px;
    color: var(--white);
    font-size: 29px;
    line-height: 41px;
    letter-spacing: 1px;
    text-transform: uppercase;
  }
  .company-name {
    position: absolute;
    left: 560px;
    width: 440px;
    top: 330px;
    text-align: center;
    color: var(--ink);
    font-weight: 400;
    font-size: 36px;
    letter-spacing: 0.5px;
    text-transform: uppercase;
  }
</style>
</head>
<body>
  <article class="business-card">
    <svg class="card-shapes" viewBox="0 0 1000 616" aria-hidden="true">
      <defs>
        <linearGradient id="paper-gradient" x1="0" y1="0" x2="1" y2="1">
          <stop offset="0" stop-color="var(--paper-shade)"/>
          <stop offset="0.45" stop-color="var(--paper-light)"/>
          <stop offset="1" stop-color="var(--white)"/>
        </linearGradient>
      </defs>
      <rect class="paper-side" width="1000" height="616" fill="url(#paper-gradient)"/>
      <polygon class="teal-panel" points="0,0 640,0 413,616 0,616" fill="var(--teal)"/>
      <line class="divider-rule" x1="656" y1="0" x2="429" y2="616" stroke="var(--rule)" stroke-width="5"/>
    </svg>

    <h1 class="holder-name">MARCUS ELLERY</h1>

    <ul class="contact-list">
      <li class="contact-item">
        <svg class="contact-icon" viewBox="0 0 24 24" aria-label="Main phone"><path d="M3 8c0-2 4-4 9-4s9 2 9 4v2h-5V8H8v2H3zM6 11h12l2 8H4z"/></svg>
        <span>+1 720 555 0147</span>
      </li>
      <li class="contact-item">
        <svg class="contact-icon" viewBox="0 0 24 24" aria-label="Cell phone"><path d="M8 2h8a2 2 0 0 1 2 2v16a2 2 0 0 1-2 2H8a2 2 0 0 1-2-2V4a2 2 0 0 1 2-2zm0 3v13h8V5zm4 14.2a1 1 0 1 0 0 1.6 1 1 0 0 0 0-1.6z"/></svg>
        <span>044-555 010 247</span>
      </li>
      <li class="contact-item">
        <svg class="contact-icon" viewBox="0 0 24 24" aria-label="Email"><path d="M3 6h18v12H3zm1.5 1.5L12 13l7.5-5.5z"/></svg>
        <span>info@quorvanecapital.example</span>
      </li>
      <li class="contact-item">
        <svg class="contact-icon" viewBox="0 0 24 24" aria-label="Website"><circle cx="12" cy="12" r="9"/><path d="M8 7c2 0 3 1 2 3s-3 1-3 3 2 3 1 5M15 5c-1 2 1 3 2 4s1 3 0 4-2 3-1 5" stroke="var(--teal)" stroke-width="1.6" fill="none"/></svg>
        <span>www.quorvanecapital.example</span>
      </li>
    </ul>

    <p class="tagline">Diversified Crypto<br>Investment Funds</p>

    <p class="company-name">Quorvane Capital</p>
  </article>
</body>
</html>
```